KTR Engineering Pty Ltd

I have already had Corvale welding and fabrication cards made , my business has changed too KTR engineering Pty Ltd so I need my logo changed on the cards
one side have my logo then the other side have what we do.
front side logo and details
owner /operator : Lachlan Meravic
email: ktr.works@ironvalemail.com
number: 0491537204
ABN: 47 261 538 902
ACN: 718 352 946
on back have in dot points what we do:
* structural steel erection
* precast panels
* site welding
*steel alteration & repair
* rigging & dogging
*labour hire
all details in breif

```html
<!DOCTYPE html>
<html lang="en">
<head>
<meta charset="utf-8">
<title>KTR Engineering Pty Ltd — Business Card</title>
<link href="https://fonts.googleapis.com/css2?family=Arimo:wght@400;700&display=swap" rel="stylesheet">
<style>
  :root {
    --backdrop: #e8e8e8;
    --card-navy: #152039;
    --card-edge: #8e2b2b;
    --accent-red: #b53a34;
    --text-white: #f2f2f2;
    --text-soft: #d6dae2;
    --divider: #8a93a6;
    --emboss: #34456a;
    --emboss-text: #6c7b9a;
  }
  html, body {
    margin: 0;
    padding: 0;
    width: 1200px;
    height: 802px;
    overflow: hidden;
    background: var(--backdrop);
    font-family: "Arimo", Arial, sans-serif;
  }
  .sheet {
    width: 1200px;
    height: 802px;
    display: flex;
    align-items: center;
    justify-content: center;
    gap: 40px;
  }
  .card {
    position: relative;
    width: 540px;
    height: 310px;
    background: var(--card-navy);
    border-bottom: 3px solid var(--card-edge);
    border-right: 2px solid var(--card-edge);
    box-sizing: border-box;
    box-shadow: 0 10px 24px rgba(0,0,0,0.18);
  }

  /* Front */
  .brand {
    position: absolute;
    left: 30px;
    top: 74px;
    width: 230px;
    text-align: right;
  }
  .brand-name {
    font-weight: 700;
    font-size: 19px;
    line-height: 1.15;
    color: var(--text-white);
    letter-spacing: 0.5px;
    text-transform: uppercase;
  }
  .brand-mark {
    display: inline-block;
    width: 10px;
    height: 10px;
    background: var(--accent-red);
    margin-left: 8px;
    vertical-align: middle;
  }
  .person {
    position: absolute;
    left: 30px;
    top: 190px;
    width: 230px;
    text-align: right;
  }
  .person-name {
    color: var(--accent-red);
    font-size: 17px;
    letter-spacing: 1px;
    text-transform: uppercase;
  }
  .person-role {
    color: var(--text-white);
    font-size: 13px;
    margin-top: 4px;
  }
  .divider {
    position: absolute;
    left: 280px;
    top: 76px;
    width: 1px;
    height: 108px;
    background: var(--divider);
  }
  .contacts {
    position: absolute;
    left: 298px;
    top: 80px;
    list-style: none;
    margin: 0;
    padding: 0;
  }
  .contacts li {
    display: flex;
    align-items: center;
    gap: 9px;
    color: var(--text-white);
    font-size: 13px;
    height: 30px;
  }
  .contacts svg { flex: none; }
  .registration {
    position: absolute;
    left: 298px;
    top: 196px;
    color: var(--text-soft);
    font-size: 12.5px;
    line-height: 1.6;
  }

  /* Back */
  .back-content {
    position: absolute;
    inset: 0;
    display: flex;
    flex-direction: column;
    align-items: center;
    justify-content: center;
    gap: 26px;
  }
  .back-brand {
    display: flex;
    align-items: center;
    gap: 12px;
  }
  .back-brand-name {
    font-weight: 700;
    font-size: 28px;
    color: var(--emboss);
    letter-spacing: 1px;
    text-transform: uppercase;
  }
  .back-brand-mark {
    width: 14px;
    height: 14px;
    background: var(--emboss);
  }
  .services {
    list-style: none;
    margin: 0;
    padding: 0;
    display: grid;
    grid-template-columns: repeat(2, 200px);
    column-gap: 24px;
    row-gap: 10px;
  }
  .services li {
    position: relative;
    padding-left: 16px;
    color: var(--emboss-text);
    font-size: 13px;
  }
  .services li::before {
    content: "";
    position: absolute;
    left: 0;
    top: 5px;
    width: 6px;
    height: 6px;
    border-radius: 50%;
    background: var(--accent-red);
  }
</style>
</head>
<body>
<main class="sheet">
  <section class="card card-front" aria-label="Card front">
    <div class="brand">
      <span class="brand-name">KTR Engineering<br>Pty Ltd</span><span class="brand-mark"></span>
    </div>
    <div class="person">
      <div class="person-name">Lachlan Meravic</div>
      <div class="person-role">Owner / Operator</div>
    </div>
    <div class="divider"></div>
    <ul class="contacts">
      <li>
        <svg width="12" height="12" viewBox="0 0 12 12" aria-hidden="true">
          <path d="M3 1.2 L4.6 3.6 L3.6 4.8 Q4.6 7 7.2 8.4 L8.4 7.4 L10.8 9 L9.8 10.8 Q5.4 10.6 1.2 4.2 Z" fill="none" stroke="var(--accent-red)" stroke-width="1.1"/>
        </svg>
        0491537204
      </li>
      <li>
        <svg width="13" height="10" viewBox="0 0 13 10" aria-hidden="true">
          <rect x="0.6" y="0.6" width="11.8" height="8.8" fill="none" stroke="var(--accent-red)" stroke-width="1.1"/>
          <path d="M0.8 0.8 L6.5 5.4 L12.2 0.8" fill="none" stroke="var(--accent-red)" stroke-width="1.1"/>
        </svg>
        ktr.works@ironvalemail.com
      </li>
      <li>
        <svg width="12" height="12" viewBox="0 0 12 12" aria-hidden="true">
          <circle cx="6" cy="6" r="5.4" fill="var(--accent-red)"/>
          <path d="M0.8 6 H11.2 M6 0.6 Q3 6 6 11.4 M6 0.6 Q9 6 6 11.4" fill="none" stroke="var(--card-navy)" stroke-width="0.8"/>
        </svg>
        www.ktrworks-site.com
      </li>
    </ul>
    <div class="registration">
      <div>ABN: 47 261 538 902</div>
      <div>ACN: 718 352 946</div>
    </div>
  </section>

  <section class="card card-back" aria-label="Card back">
    <div class="back-content">
      <div class="back-brand">
        <span class="back-brand-name">KTR Engineering Pty Ltd</span>
        <span class="back-brand-mark"></span>
      </div>
      <ul class="services">
        <li>Structural steel erection</li>
        <li>Precast panels</li>
        <li>Site welding</li>
        <li>Steel alteration &amp; repair</li>
        <li>Rigging &amp; dogging</li>
        <li>Labour hire</li>
      </ul>
    </div>
  </section>
</main>
</body>
</html>
```